New Architectural Firm Business Cards

New Business card to compliment previous pixel forum logo (attached). Please design a business card that is simple, modern, creative....please do not use "symbols", simply the logo and associated graphics/text. The front should contain name/address/phone/email/web address (with graphics).....back should be 100% graphic design using the logo somehow. Hoping for a two color (black and yellow) design. full bleed design, no borders

Target Market(s)

Commercial Architecture Clients

Industry/Entity Type

Architecture

Contact Information for Business Card

Please design a business card that is simple, modern, creative....please do not use "symbols", simply the logo and associated graphics/text. The front should contain name/address/phone/email/web address (with graphics).....back should be 100% graphic design using the logo somehow

Font styles to use
Sans Serif

Colors
FFF300
FFF600
FEFA6F
FFFEC7
FFFEE8

Requirements
Must have
• Clean, Modern Design
Should not have
• Stock images or "icons"

```html
<!DOCTYPE html>
<html lang="en">
<head>
<meta charset="utf-8">
<title>Pixel Forum Architecture – Business Cards</title>
<link href="https://fonts.googleapis.com/css2?family=Poppins:wght@400;500;600&display=swap" rel="stylesheet">
<style>
  :root {
    --backdrop: #0e0e0e;
    --card: #2a2a2c;
    --card-deep: #262628;
    --yellow: #f8c215;
    --white: #f2f2f2;
    --muted: #d9d9d9;
    --rule: #4a4a4c;
    --emboss: #3a3a3d;
    --emboss-light: #4a4a4d;
  }
  * { box-sizing: border-box; margin: 0; padding: 0; }
  html, body { width: 1200px; height: 820px; overflow: hidden; }
  body {
    background: var(--backdrop);
    font-family: "Poppins", sans-serif;
    position: relative;
  }
  .card {
    position: absolute;
    top: 250px;
    width: 540px;
    height: 310px;
    background: var(--card);
    box-shadow: 0 18px 40px rgba(0,0,0,.6);
  }
  .card-front { left: 40px; border-left: 2px solid var(--yellow); border-bottom: 2px solid var(--yellow); }
  .card-back { left: 620px; background: var(--card-deep); border-bottom: 4px solid var(--yellow); }

  /* Front – brand lock-up */
  .brand {
    position: absolute;
    right: 40px;
    top: 42px;
    text-align: right;
  }
  .brand-name {
    display: flex;
    align-items: center;
    justify-content: flex-end;
    gap: 10px;
    color: var(--yellow);
    font-weight: 600;
    font-size: 38px;
    line-height: 1;
    letter-spacing: .5px;
  }
  .brand-dot { width: 22px; height: 22px; border-radius: 50%; background: var(--yellow); }
  .brand-sub {
    margin-top: 8px;
    color: var(--white);
    font-weight: 600;
    font-size: 22px;
    letter-spacing: 1px;
  }
  .divider-main {
    position: absolute;
    left: 150px; right: 40px; top: 160px;
    height: 1px; background: var(--rule);
  }

  /* Front – person */
  .person { position: absolute; left: 36px; top: 188px; }
  .person-name { color: var(--yellow); font-weight: 600; font-size: 19px; letter-spacing: .3px; line-height: 1.1; }
  .person-role { color: var(--white); font-size: 14px; margin-top: 2px; }
  .divider-person { width: 140px; height: 1px; background: var(--rule); margin: 10px 0 8px; }
  .contact-list { list-style: none; }
  .contact-item {
    display: flex; align-items: center; gap: 8px;
    color: var(--muted); font-size: 13.5px; line-height: 1.45;
  }
  .contact-icon { width: 13px; height: 13px; flex: none; }

  .address {
    position: absolute;
    right: 40px; top: 196px;
    text-align: right;
    color: var(--muted);
    font-size: 13.5px;
    line-height: 1.45;
  }

  /* Back – embossed lock-up */
  .emboss {
    position: absolute;
    left: 0; right: 0; top: 108px;
    text-align: center;
  }
  .emboss-name {
    display: inline-flex; align-items: center; gap: 12px;
    color: var(--emboss); font-weight: 600; font-size: 46px; line-height: 1;
  }
  .emboss-dot { width: 26px; height: 26px; border-radius: 50%; background: var(--emboss); }
  .emboss-sub {
    margin-top: 10px;
    color: var(--emboss-light); font-weight: 600; font-size: 22px; letter-spacing: 1px;
  }
</style>
</head>
<body>

<section class="card card-front" aria-label="Business card front">
  <div class="brand">
    <div class="brand-name"><span class="brand-dot"></span>PIXEL FORUM</div>
    <div class="brand-sub">ARCHITECTURE</div>
  </div>
  <div class="divider-main"></div>

  <div class="person">
    <p class="person-name">MARCUS HALE</p>
    <p class="person-role">Managing Director</p>
    <div class="divider-person"></div>
    <ul class="contact-list">
      <li class="contact-item">
        <svg class="contact-icon" viewBox="0 0 16 16" aria-hidden="true"><path fill="#f8c215" d="M3.5 1.5l2.5 3-1.5 1.6a9 9 0 0 0 5.4 5.4L11.5 10l3 2.5-1.6 2.3C7 14.3 1.7 9 1.2 3.1z"/></svg>
        055-210 334 876
      </li>
      <li class="contact-item">
        <svg class="contact-icon" viewBox="0 0 16 16" aria-hidden="true"><rect x="1" y="3" width="14" height="10" fill="#f8c215"/><path d="M1 3l7 6 7-6" fill="none" stroke="#2a2a2c" stroke-width="1.4"/></svg>
        hello@pixelforum.com
      </li>
      <li class="contact-item">
        <svg class="contact-icon" viewBox="0 0 16 16" aria-hidden="true"><g fill="none" stroke="#f8c215" stroke-width="1.4"><circle cx="8" cy="8" r="6.5"/><ellipse cx="8" cy="8" rx="3" ry="6.5"/><path d="M1.5 8h13M2.5 4.8h11M2.5 11.2h11"/></g></svg>
        www.pixelforum.com
      </li>
    </ul>
  </div>

  <div class="address">
    <p>18, Harbour Row Lane</p>
    <p>30917, Eastmere</p>
  </div>
</section>

<section class="card card-back" aria-label="Business card back">
  <div class="emboss">
    <div class="emboss-name"><span class="emboss-dot"></span>PIXEL FORUM</div>
    <div class="emboss-sub">ARCHITECTURE</div>
  </div>
</section>

</body>
</html>
```